Photography Business, Business Card

Looking for a unique cutting edge card that takes advantage of the latest printing technologies. Please review this site for all the options they office: https://plumeprints.example. If you can think it they can do it. And if you have an idea and do not know if they can do it, I will check into it.
Updates

Target Market(s)

People and places I took images of and future clients.

Industry/Entity Type

Photography

Contact Information for Business Card

Name, cell & email. Colin Hartley, chartley@kvnphoto.example, 318-742-9061

Colors

Designer to choose only greyscale colors for use in the design.

Requirements
Must have
• 100% cutting edge. Is so great, those I hand it to always show it to someone else. A piece of art.
Nice to have
• Blacks, silvers, greys, some red. Maybe other colors?

```html
<!DOCTYPE html>
<html lang="en">
<head>
<meta charset="utf-8">
<title>Colin Hartley — Business Card</title>
<link rel="stylesheet" href="https://fonts.googleapis.com/css2?family=PT+Sans&family=Questrial&display=swap">
<style>
  :root {
    --page: #ffffff;
    --card: #efeff0;
    --card-edge: #a9a9ab;
    --band-dark: #1c1c1c;
    --band-mid: #2e2e2e;
    --ink: #111111;
    --light-text: #e6e6e6;
    --accent: #d9262c;
    --lens-fill-top: #2a2626;
    --lens-fill-bottom: #121212;
  }
  html, body {
    margin: 0;
    padding: 0;
    width: 1200px;
    height: 1200px;
    overflow: hidden;
    background: var(--page);
  }
  .canvas {
    position: relative;
    width: 1200px;
    height: 1200px;
  }
  .side-label {
    position: absolute;
    margin: 0;
    font-family: "PT Sans", sans-serif;
    font-weight: 400;
    font-size: 48px;
    line-height: 1;
    color: var(--ink);
  }
  .side-label--front { left: 126px; top: 146px; }
  .side-label--back { left: 814px; top: 482px; }

  .card {
    position: absolute;
    width: 269px;
    height: 440px;
    box-sizing: border-box;
    background: var(--card);
    border: 1.5px solid var(--card-edge);
    border-radius: 134.5px 134.5px 0 0;
    overflow: hidden;
  }
  .card--front { left: 115px; top: 220px; }
  .card--back { left: 799px; top: 554px; }

  .card__lens {
    position: absolute;
    left: 32px;
    top: 32px;
    width: 204px;
    height: 204px;
    border-radius: 50%;
    background: linear-gradient(180deg, var(--lens-fill-top), var(--lens-fill-bottom));
  }

  .card__band {
    position: absolute;
    left: 0;
    right: 0;
    bottom: 0;
    height: 101px;
    background: linear-gradient(180deg, var(--band-mid), var(--band-dark));
    font-family: "Questrial", sans-serif;
    color: var(--light-text);
    text-align: center;
  }

  .brand-name {
    display: block;
    margin-top: 22px;
    font-size: 30px;
    letter-spacing: 4px;
    line-height: 1;
    color: var(--accent);
  }
  .person-name {
    display: block;
    margin-top: 6px;
    font-size: 24px;
    letter-spacing: 0.5px;
    line-height: 1;
  }

  .contact-list {
    list-style: none;
    margin: 0;
    padding: 26px 0 0;
    font-size: 16px;
    line-height: 1;
  }
  .contact-list li {
    display: flex;
    align-items: center;
    justify-content: center;
    gap: 10px;
  }
  .contact-list li + li { margin-top: 21px; }
  .contact-icon { flex: none; }
</style>
</head>
<body>
<main class="canvas">

  <h2 class="side-label side-label--front">front side</h2>
  <section class="card card--front" aria-label="Card front">
    <div class="card__lens" role="img" aria-label="Camera lens illustration"></div>
    <div class="card__band">
      <span class="brand-name">KVN</span>
      <span class="person-name">Colin Hartley</span>
    </div>
  </section>

  <h2 class="side-label side-label--back">back side</h2>
  <section class="card card--back" aria-label="Card back">
    <div class="card__lens" role="img" aria-label="Camera lens illustration"></div>
    <div class="card__band">
      <ul class="contact-list">
        <li>
          <svg class="contact-icon" width="16" height="16" viewBox="0 0 24 24" aria-hidden="true">
            <path fill="var(--accent)" d="M6.6 10.8a15.1 15.1 0 0 0 6.6 6.6l2.2-2.2c.3-.3.7-.4 1-.2 1.1.4 2.3.6 3.6.6.6 0 1 .4 1 1V20c0 .6-.4 1-1 1A17 17 0 0 1 3 4c0-.6.4-1 1-1h3.5c.6 0 1 .4 1 1 0 1.3.2 2.5.6 3.6.1.3 0 .7-.2 1z"/>
          </svg>
          <span>318-742-9061</span>
        </li>
        <li>
          <svg class="contact-icon" width="16" height="12" viewBox="0 0 16 12" aria-hidden="true">
            <rect width="16" height="12" rx="1.5" fill="var(--accent)"/>
            <path d="M1 1.5 8 6.5l7-5" fill="none" stroke="var(--band-dark)" stroke-width="1.2"/>
          </svg>
          <span>chartley@kvnphoto.example</span>
        </li>
      </ul>
    </div>
  </section>

</main>
</body>
</html>
```